MyName is TapKard .... Killer of Business Cards!!! WANT a KickAss Design Landing Page :)

How 'TapKard' works:
- with a unique name for each country, like a personalise car plate number
- our platform links through a 'Quick Text' keyword short code
- TapKard platform will respond with downloaded ready full contact business file link
- this is designed to be downloaded in just '3 clicks' into your Contacts Folder
- any changes,,updates, images, online profiles can be made in real time updates
- TapKard provides a backend login to manage individual account and is ready
Enterprise model for larger staff companies
- platform is international ready and have launched
Australia, in September 2019.

Yes, your whole business card and online profile in '3' simple clicks. No '20-30 mins' of typing the business card contacts details into mobile phones.
** Fact: 88% of business cards are lost of thrown out within 7 days.
(https://www.ledgerowl.example/business-card-statistics.html) **

NZ ClipTube
https://clipwave.example/v/qr8Lm2Tz4Xa

**current websites are www.tkard.co.nz www.tapcard.com.au www.tapkardau.com www.tapkardus.com **

Target Market(s)

Anybody who uses a business card, from trades person, real estate agents, consultants, bankers (in NZ/AU with have plumbers, financial advisors, real estate agents, mortgage brokers, sports agents, Telcos etc etc)

Industry/Entity Type

Business Software

Coding

Coded - Design and coding required

Number of Pages Required

4 page

Font styles to use
Other font styles liked:
• libre franklin black

Requirements
Must have
• TapKard a simple 'in delivery' and smart 'in innovation' solution so our message is Simple, Clear and Inquisitive. We would like a converting landing page because we are selling Quick Cloud Suite at low-entry cost and no-contract. IWe want to direct clients to a name reservation platform to a virtual business card that uses our Quick Private Suite. We will require some code at the back to link the name reservation and sign up source code(javascript). This web/landing page fresh page is required because we have recently changed our marketing strategy to be purely digital marketing in Friendloop and Snapgrid Ads from now on. We would like this to be exciting graphically to grab attention, inquisitive enough to check your name availability and follow through with call to action with the right colours and graphics images. We plan to test the right pitch offering until we get the markets feedback on the best offering/re-design and then push harder with more FL and SG Ads. ( **we plan to continue multiple regular campaigns as the business has now change our strategy due to covid-19 and we will focus mainly on direct to consumers**)

Also:
2 buttons: Signup and a Check availability little form to allow a java script to be added/HTML5/FL advertising/Super Inviting to check 'YOUR UNIQUE NAME' is available. Then clicking the to reserve the name to purchase our Quick Text/Eco-Friendly/Relevant to todays tech and Low Cost service. We will be offering Promo codes for each campaign.
No Apps. Works with SMS, any smartphone, country specific, enterprise ready, and CONTACTLESS ....
Nice to have
• Personal feeling. Unique choice of 'your name' as this is your business and social profile in one. Strong independent images and confident to share with anybody their profile by just sharing their name.
Should not have
• Open currently....

```html
<!DOCTYPE html>
<html lang="en">
<head>
<meta charset="utf-8">
<title>TapKard – Your name is your business card</title>
<link href="https://fonts.googleapis.com/css2?family=Poppins:wght@400;500;600;700&display=swap" rel="stylesheet">
<style>
:root{
  --navy:#1f3468;
  --navy-deep:#1a2d5c;
  --teal:#138f8f;
  --orange:#f5901e;
  --ink:#1d1f2b;
  --muted:#8a8d99;
  --line:#e6e7ec;
  --soft:#f3f3f5;
  --white:#ffffff;
}
*{margin:0;padding:0;box-sizing:border-box}
html,body{width:1200px;height:2659px;overflow:hidden}
body{font-family:'Poppins',sans-serif;color:var(--ink);background:var(--navy);position:relative}
.backdrop-light{position:absolute;left:0;top:477px;width:1200px;height:1485px;background:#f7f7f9}
.page{position:absolute;left:242px;top:147px;width:715px;height:2366px;background:var(--white);box-shadow:0 0 40px rgba(0,0,0,.18)}
.abs{position:absolute}
.center{text-align:center}

/* nav */
.nav{left:0;top:0;width:715px;height:43px;background:var(--white)}
.brand{left:87px;top:11px;display:flex;align-items:center;gap:5px;font-size:13px;font-weight:600;color:var(--navy)}
.brand-dot{width:14px;height:14px;border-radius:50%;border:2px solid var(--teal)}
.nav-link{top:16px;font-size:7.5px;font-weight:500;color:#555a6b}
.btn-signin{left:567px;top:10px;width:64px;height:21px;background:var(--navy);color:#fff;font-size:7.5px;font-weight:600;display:flex;align-items:center;justify-content:center;border:1px solid #0f1d42}

/* hero */
.hero{left:0;top:43px;width:715px;height:287px;background:linear-gradient(160deg,#3c4f87,#2a3e78 55%,#34467f);overflow:hidden}
.hero-tint{left:0;top:0;width:715px;height:287px;background:rgba(31,52,104,.55)}
.hero-title{left:0;top:44px;width:715px;font-size:19px;font-weight:600;line-height:18px;color:#fff}
.hero-copy{left:112px;width:491px;font-size:7.2px;line-height:9.5px;color:#fff}
.search{left:199px;top:209px;width:318px;height:31px;background:#fff;border:2px solid #fff}
.search-input{left:12px;top:8px;font-size:8px;color:#a7a9b3}
.search-btn{left:218px;top:0;width:96px;height:27px;background:var(--navy);color:#fff;font-size:7.3px;font-weight:600;display:flex;align-items:center;justify-content:center}

/* video */
.video{left:179px;top:370px;width:357px;height:201px;background:linear-gradient(120deg,#5b6478 0%,#3a5e8c 45%,#2a78b4 100%)}

/* headings */
.section-title{left:0;width:715px;font-size:14.5px;font-weight:600;color:var(--ink)}
.section-sub{left:0;width:715px;font-size:9px;color:#b2b4bc}

/* benefits */
.benefit{width:173px;height:123px;border:1px solid var(--line);background:#fff}
.benefit.is-raised{background:#fafafb;box-shadow:0 4px 14px rgba(0,0,0,.06)}
.benefit-icon{left:66px;top:12px;width:40px;height:40px;border-radius:50%;background:#fff;box-shadow:0 2px 8px rgba(0,0,0,.1);display:flex;align-items:center;justify-content:center}
.benefit-name{left:0;top:59px;width:171px;font-size:9.5px;font-weight:600;color:var(--ink)}
.benefit-text{left:20px;top:74px;width:131px;font-size:6.3px;line-height:8.5px;color:var(--muted)}
.btn-benefits{left:291px;top:937px;width:137px;height:37px;background:var(--navy);color:#fff;font-size:10px;font-weight:500;display:flex;align-items:center;justify-content:center;border-radius:2px}

/* partners */
.partners{left:0;top:1016px;width:715px;height:245px;background:var(--soft)}
.partner-mark{display:flex;align-items:center;justify-content:center;gap:6px;font-weight:600;width:240px}
.partner-circle{width:22px;height:22px;border-radius:50%;background:var(--teal)}
.partner-square{width:20px;height:20px;background:#e6a91a}
.partner-name{width:240px;font-size:10px;font-weight:600;color:var(--ink)}
.partner-text{width:232px;font-size:6.2px;line-height:9.6px;color:var(--muted)}

/* plans */
.plan-board{width:139px}
.plan-art{left:0;top:0;width:139px;height:86px}
.plan-card{width:173px;background:#fff;box-shadow:0 6px 14px rgba(0,0,0,.12)}
.plan-name{left:0;top:33px;width:173px;font-size:16px;font-weight:500}
.plan-price{left:0;top:52px;width:173px;font-size:26px;font-weight:600}
.plan-text{left:12px;top:95px;width:149px;font-size:9.4px;line-height:11px;color:#676a75}
.plan-btn{left:17px;width:139px;height:35px;color:#fff;font-size:13px;font-weight:500;display:flex;align-items:center;justify-content:center;border-radius:2px}
.is-teal{color:var(--teal)} .bg-teal{background:var(--teal)}
.is-orange{color:var(--orange)} .bg-orange{background:var(--orange)}
.is-navy{color:var(--navy)} .bg-navy{background:var(--navy)}

/* testimonials */
.testimonials{left:0;top:1815px;width:715px;height:322px;background:var(--navy)}
.testimonials .section-title{color:#fff}
.quote-card{top:75px;width:167px;height:180px;background:#fff;border-radius:6px}
.quote-mark{left:69px;top:28px;width:29px;height:22px}
.quote-name{left:0;top:58px;width:167px;font-size:9.6px;font-weight:600;color:var(--ink)}
.quote-role{left:0;top:71px;width:167px;font-size:8.4px;color:#6c6f7a}
.quote-text{left:30px;top:89px;width:107px;font-size:6.7px;line-height:9.7px;color:var(--muted)}
.avatar{left:58px;top:156px;width:50px;height:50px;border-radius:50%;border:3px solid #fff;background:linear-gradient(160deg,#8a6a5a,#d8b5a0)}

/* footer */
.footer{left:0;top:2137px;width:715px;height:229px;background:#fff}
.footer-col{top:48px}
.footer-head{font-size:8px;font-weight:600;color:var(--ink);margin-bottom:9px;text-transform:uppercase}
.footer-link{font-size:6.3px;color:var(--muted);line-height:16px;padding-left:3px}
.footer-contact{font-size:5.6px;color:var(--muted);line-height:7px;padding-left:3px;margin-bottom:5px;width:100px}
.pay-row{left:87px;top:155px;width:545px;height:33px;border-top:1px solid var(--line);border-bottom:1px solid var(--line);display:flex;align-items:center;justify-content:space-between}
.pay-label{font-size:7px;font-weight:500;color:var(--ink)}
.pay-name{font-size:7.5px;font-weight:600;color:var(--navy)}
.copyright{left:87px;top:200px;font-size:6.3px;color:#555a6b}
.social{left:560px;top:199px;display:flex;gap:8px;font-size:6.3px;font-weight:600;color:var(--ink)}
</style>
</head>
<body>
<div class="backdrop-light"></div>

<main class="page">
  <!-- navigation -->
  <header class="nav abs">
    <div class="brand abs"><span class="brand-dot"></span>TapKard</div>
    <span class="nav-link abs" style="left:313px">Partners</span>
    <span class="nav-link abs" style="left:368px">Benefits</span>
    <span class="nav-link abs" style="left:420px">Plans</span>
    <span class="nav-link abs" style="left:464px">Testimonials</span>
    <span class="nav-link abs" style="left:535px">Log In</span>
    <a class="btn-signin abs">Sign In</a>
  </header>

  <!-- hero -->
  <section class="hero abs" role="img" aria-label="Collage of smiling business people holding phones">
    <div class="hero-tint abs"></div>
    <h1 class="hero-title abs center">Simply say: Txt 'Name' or<br>'Business Name' to 552.</h1>
    <p class="hero-copy abs center" style="top:97px">90% of the worlds 10 Billion business cards, are thrown away with 7 days. What a waste of paper and money!<br>'Virtual Business Card' or 'TapKard' is the Digital Solution.</p>
    <p class="hero-copy abs center" style="top:126px">TapKard is the intelligent, relevant and easy way for your new customers or friends to receive ALL of your contact card information<br>and in to a few clicks, be saved to their phones. This can be done anytime and anywhere, within New Zealand.</p>
    <p class="hero-copy abs center" style="top:155px">Some TapKard clients advertise this powerful tool for their business on vehicles, billboards, store frontage, websites, social media,<br>company uniforms or just anywhere (ie text 'builder' to 552).</p>
    <p class="hero-copy abs center" style="top:184px">TapKard - Simple, Low Cost, Smart and Effective!</p>
    <form class="search abs">
      <span class="search-input abs">Your Keyword</span>
      <span class="search-btn abs">Check Availability</span>
    </form>
  </section>

  <!-- video -->
  <div class="video abs" role="img" aria-label="Video preview: hand holding a phone showing a TapKard contact, headline Business Cards are over, See what's in"></div>

  <!-- benefits -->
  <h2 class="section-title abs center" style="top:609px">Simple Benefits Are</h2>

  <article class="benefit abs" style="left:89px;top:649px">
    <div class="benefit-icon abs"><svg width="18" height="18" viewBox="0 0 18 18" fill="none" stroke="#1f3468" stroke-width="1.2"><rect x="5" y="2" width="8" height="14" rx="1.5"/><line x1="8" y1="13.5" x2="10" y2="13.5"/></svg></div>
    <h3 class="benefit-name abs center">Logical</h3>
    <p class="benefit-text abs center">Everybody has a mobile phone and every phone can txt/sms.</p>
  </article>
  <article class="benefit is-raised abs" style="left:272px;top:649px">
    <div class="benefit-icon abs"><svg width="18" height="18" viewBox="0 0 18 18" fill="none" stroke="#1f3468" stroke-width="1.2"><path d="M9 2a5 5 0 0 0-3 9v2h6v-2a5 5 0 0 0-3-9z"/><line x1="7" y1="15.5" x2="11" y2="15.5"/></svg></div>
    <h3 class="benefit-name abs center">Professional</h3>
    <p class="benefit-text abs center">Your customers / potential customers will be impressed with your innovation.</p>
  </article>
  <article class="benefit abs" style="left:457px;top:649px">
    <div class="benefit-icon abs"><svg width="18" height="18" viewBox="0 0 18 18" fill="none" stroke="#1f3468" stroke-width="1.2"><rect x="3" y="3" width="12" height="12" rx="1"/><line x1="6" y1="7" x2="12" y2="7"/><line x1="6" y1="10" x2="12" y2="10"/></svg></div>
    <h3 class="benefit-name abs center">Environment</h3>
    <p class="benefit-text abs center">No use of business cards, you no longer need to have cards printed, thus reducing your carbon foot print.</p>
  </article>
  <article class="benefit abs" style="left:89px;top:784px">
    <div class="benefit-icon abs"><svg width="18" height="18" viewBox="0 0 18 18" fill="none" stroke="#1f3468" stroke-width="1.2"><rect x="2" y="5" width="14" height="9" rx="1"/><line x1="5" y1="8" x2="10" y2="8"/><line x1="5" y1="11" x2="8" y2="11"/></svg></div>
    <h3 class="benefit-name abs center">Ease</h3>
    <p class="benefit-text abs center">So simple to share and retrieve your TapKard.</p>
  </article>
  <article class="benefit abs" style="left:272px;top:784px">
    <div class="benefit-icon abs"><svg width="18" height="18" viewBox="0 0 18 18" fill="none" stroke="#1f3468" stroke-width="1.2"><polyline points="3,13 7,9 10,11 15,5"/><polyline points="11,5 15,5 15,9"/></svg></div>
    <h3 class="benefit-name abs center">Sales</h3>
    <p class="benefit-text abs center">May increase your sales by word of mouth, added to your advertising and ability to share TapKard anywhere.</p>
  </article>
  <article class="benefit abs" style="left:457px;top:784px">
    <div class="benefit-icon abs"><svg width="18" height="18" viewBox="0 0 18 18" fill="none" stroke="#1f3468" stroke-width="1.2"><circle cx="9" cy="9" r="6"/><path d="M11 6.5H8a1.3 1.3 0 0 0 0 2.6h2a1.3 1.3 0 0 1 0 2.6H7"/><line x1="9" y1="5" x2="9" y2="13"/></svg></div>
    <h3 class="benefit-name abs center">Cost</h3>
    <p class="benefit-text abs center">The service is less per year than the average sales persons cost in business cards</p>
  </article>

  <a class="btn-benefits abs">See All Benefits</a>

  <!-- partners -->
  <section class="partners abs">
    <h2 class="section-title abs center" style="top:31px">Our Partners</h2>
    <div class="partner-mark abs is-teal" style="left:101px;top:86px;font-size:16px"><span class="partner-circle"></span>FindBack</div>
    <div class="partner-mark abs" style="left:378px;top:83px;font-size:20px;color:#e6a91a"><span class="partner-square"></span>Startwell</div>
    <h3 class="partner-name abs center" style="left:101px;top:119px">Find Back</h3>
    <h3 class="partner-name abs center" style="left:378px;top:119px">Startwell</h3>
    <p class="partner-text abs center" style="left:105px;top:138px">FindBack is the World's Largest Global Recovery company which helps return lost items to their rightful owners. With over an 80% recovery rate, FindBack recovery tags help identify and protect all types of portable items ranging from cell phones to laptops, keys to luggage and even cats &amp; dogs. FindBack's system is simple, convenient, confidential and rewarding!</p>
    <p class="partner-text abs center" style="left:382px;top:138px">Startwell is a one-stop-shop, easy-to-use web platform to assist those wanting to start a business but do not know-how. Startwell is an affordable platform that takes you through all the steps you need to incorporate a business, register with IRD, obtain urls, design a logo and website, as well as set up your email, an eCommerce platform, a payment gateway and link to industry leading accounting packages - that is, everything you need to get you market-ready.</p>
  </section>

  <!-- plans -->
  <h2 class="section-title abs center" style="top:1320px">Plans For Everyone</h2>
  <p class="section-sub abs center" style="top:1340px">with great pricing</p>

  <div class="plan-board abs bg-teal" style="left:106px;top:1412px;height:352px">
    <div class="plan-art abs" role="img" aria-label="Paper plane flying among clouds" style="background:linear-gradient(180deg,#16999a,#118686)"></div>
  </div>
  <div class="plan-board abs bg-orange" style="left:289px;top:1377px;height:353px">
    <div class="plan-art abs" role="img" aria-label="Passenger airplane flying among clouds" style="background:linear-gradient(180deg,#f79a2c,#f08a16)"></div>
  </div>
  <div class="plan-board abs bg-navy" style="left:474px;top:1412px;height:352px">
    <div class="plan-art abs" role="img" aria-label="Rocket flying among clouds" style="background:linear-gradient(180deg,#243b74,#1c305f)"></div>
  </div>

  <article class="plan-card abs" style="left:89px;top:1498px;height:206px">
    <h3 class="plan-name abs center is-teal">BASIC</h3>
    <p class="plan-price abs center is-teal">$4.99/m</p>
    <p class="plan-text abs center">Provides for one keyword and one personal TapKard.</p>
    <a class="plan-btn abs bg-teal" style="top:145px">BUY NOW</a>
  </article>
  <article class="plan-card abs" style="left:273px;top:1463px;height:213px">
    <h3 class="plan-name abs center is-orange">ADVANCE</h3>
    <p class="plan-price abs center is-orange">$6.99/m</p>
    <p class="plan-text abs center">Provides for one personal and business keyword.</p>
    <a class="plan-btn abs bg-orange" style="top:145px">BUY NOW</a>
  </article>
  <article class="plan-card abs" style="left:457px;top:1498px;height:211px">
    <h3 class="plan-name abs center is-navy">PRO</h3>
    <p class="plan-price abs center is-navy">$9.99/m</p>
    <p class="plan-text abs center">Provides for one keyword and one personal TapKard.</p>
    <a class="plan-btn abs bg-navy" style="top:150px">BUY NOW</a>
  </article>

  <!-- testimonials -->
  <section class="testimonials abs">
    <h2 class="section-title abs center" style="top:35px">Our Clients love us!</h2>
    <article class="quote-card abs" style="left:89px">
      <svg class="quote-mark abs" viewBox="0 0 29 22" fill="#1f3468"><path d="M0 14a6 6 0 1 0 6-6c0-3 2-5 5-6V0C5 1 0 6 0 14z"/><path d="M16 14a6 6 0 1 0 6-6c0-3 2-5 5-6V0c-6 1-11 6-11 14z"/></svg>
      <h3 class="quote-name abs center">MARA LIND</h3>
      <p class="quote-role abs center">KL Marketing</p>
      <p class="quote-text abs center">LorLorem Ipsum is simply dummy text of the printing and typesetting industry. Lorem Ipsum has been the industry's standard.</p>
      <div class="avatar abs" role="img" aria-label="Client portrait"></div>
    </article>
    <article class="quote-card abs" style="left:276px">
      <svg class="quote-mark abs" viewBox="0 0 29 22" fill="#1f3468"><path d="M0 14a6 6 0 1 0 6-6c0-3 2-5 5-6V0C5 1 0 6 0 14z"/><path d="M16 14a6 6 0 1 0 6-6c0-3 2-5 5-6V0c-6 1-11 6-11 14z"/></svg>
      <h3 class="quote-name abs center">MARA LIND</h3>
      <p class="quote-role abs center">KL Marketing</p>
      <p class="quote-text abs center">LorLorem Ipsum is simply dummy text of the printing and typesetting industry. Lorem Ipsum has been the industry's standard.</p>
      <div class="avatar abs" role="img" aria-label="Client portrait"></div>
    </article>
    <article class="quote-card abs" style="left:463px">
      <svg class="quote-mark abs" viewBox="0 0 29 22" fill="#1f3468"><path d="M0 14a6 6 0 1 0 6-6c0-3 2-5 5-6V0C5 1 0 6 0 14z"/><path d="M16 14a6 6 0 1 0 6-6c0-3 2-5 5-6V0c-6 1-11 6-11 14z"/></svg>
      <h3 class="quote-name abs center">MARA LIND</h3>
      <p class="quote-role abs center">KL Marketing</p>
      <p class="quote-text abs center">LorLorem Ipsum is simply dummy text of the printing and typesetting industry. Lorem Ipsum has been the industry's standard.</p>
      <div class="avatar abs" role="img" aria-label="Client portrait"></div>
    </article>
  </section>

  <!-- footer -->
  <footer class="footer abs">
    <div class="footer-col abs" style="left:85px">
      <h4 class="footer-head">Quick Links</h4>
      <p class="footer-link">Home</p><p class="footer-link">About Us</p><p class="footer-link">Privacy Policy</p><p class="footer-link">Terms &amp; Condition</p><p class="footer-link">Contact Us</p>
    </div>
    <div class="footer-col abs" style="left:224px">
      <h4 class="footer-head">Useful Links</h4>
      <p class="footer-link">Home</p><p class="footer-link">About Us</p><p class="footer-link">Privacy Policy</p><p class="footer-link">Terms &amp; Condition</p><p class="footer-link">Contact Us</p>
    </div>
    <div class="footer-col abs" style="left:366px">
      <h4 class="footer-head">All Products</h4>
      <p class="footer-link">TapKard For ID NSW</p><p class="footer-link">TapKard For ID QLD</p><p class="footer-link">TapKard For ID ACT</p><p class="footer-link">TapKard For ID PERTH</p><p class="footer-link">TapKard For ID SA</p>
    </div>
    <div class="footer-col abs" style="left:503px">
      <h4 class="footer-head">Contact Us</h4>
      <p class="footer-contact">Email: support@tkard.co.nz</p>
      <p class="footer-contact">NZBN: 9400000000001</p>
      <p class="footer-contact">GST: 100 - 200 - 300</p>
      <p class="footer-contact">PO Box 100 200 | Harbourside | Auckland 2010</p>
      <p class="footer-contact">7B / 42 Kowhai Road | Eastvale Auckland 2013</p>
    </div>
    <div class="pay-row abs">
      <span class="pay-label">Payment Options</span>
      <span class="pay-name">Mintrel</span>
      <span class="pay-name">Payvane</span>
      <span class="pay-name">Zeppo</span>
      <span class="pay-name">Veltrix</span>
      <span class="pay-name">Corvane</span>
      <span class="pay-name">Laterly</span>
    </div>
    <p class="copyright abs">Copyright © 2020 TapKard</p>
    <div class="social abs"><span>Friendloop</span><span>Chirper</span><span>Snapgrid</span></div>
  </footer>
</main>
</body>
</html>
```